Simple AD for Digital Publication

Total Size 5" x 5", may include boarder or not
Image Provided; crop or use as background
Incorporate Logo and text as provided

Target Market(s)

Sound Contractors / Integrators

Industry/Entity Type

Audio Video Lighting

Requirements
Must have
• Bold Look that reflects our brand. see website: tovermundic.com - cohesive text and style

```html
<!DOCTYPE html>
<html lang="en">
<head>
<meta charset="utf-8">
<title>Tovermundic Co – Become a Dealer</title>
<link rel="stylesheet" href="https://fonts.googleapis.com/css2?family=Montserrat:wght@600;700;800&display=swap">
<style>
  :root {
    --brand-red: #ae0000;
    --brand-red-light: #bd1a1a;
    --white: #ffffff;
    --panel-grey: #e8ecea;
    --band-grey: #4b4b4b;
    --ink-dark: #3a3a3a;
    --dot: rgba(255, 255, 255, 0.9);
  }
  * { margin: 0; padding: 0; box-sizing: border-box; }
  html, body { width: 1200px; height: 1200px; overflow: hidden; background: var(--brand-red); }
  .ad {
    position: relative;
    width: 1200px;
    height: 1200px;
    background: var(--brand-red);
    font-family: "Montserrat", Arial, sans-serif;
    overflow: hidden;
  }
  .ad__chevrons { position: absolute; left: 0; top: 0; }
  .ad__headline {
    position: absolute;
    top: 104px;
    left: 0;
    width: 100%;
    text-align: center;
    color: var(--white);
    font-weight: 700;
    font-size: 52px;
    line-height: 62px;
    letter-spacing: 1.5px;
    text-shadow: 0 3px 6px rgba(0,0,0,0.25);
  }
  .ad__dots { position: absolute; top: 503px; }
  .ad__dots--left { left: 26px; }
  .ad__dots--right { left: 998px; }
  .ad__product-photo {
    position: absolute;
    left: 291px;
    top: 260px;
    width: 618px;
    height: 618px;
    border-radius: 50%;
    border: 8px solid var(--white);
    background:
      radial-gradient(ellipse 60% 30% at 55% 28%, rgba(255, 226, 160, 0.55), transparent 70%),
      linear-gradient(180deg, #3d2a1c 0%, #2d4a22 18%, #3f6a2a 40%, #7a6a58 55%, #b9aa9b 70%, #8f8072 100%);
    box-shadow: 0 6px 18px rgba(0,0,0,0.25);
  }
  .ad__cta-label {
    position: absolute;
    top: 900px;
    left: 0;
    width: 100%;
    text-align: center;
    color: var(--white);
    font-weight: 700;
    font-size: 31px;
  }
  .ad__cta-button {
    position: absolute;
    left: 363px;
    top: 948px;
    width: 463px;
    height: 64px;
    border-radius: 32px;
    background: var(--white);
    color: var(--brand-red);
    font-weight: 700;
    font-size: 36px;
    letter-spacing: 1px;
    display: flex;
    align-items: center;
    justify-content: center;
    text-decoration: none;
    box-shadow: 0 4px 10px rgba(0,0,0,0.25);
  }
  .ad__footer { position: absolute; left: 0; top: 0; }
  .brand {
    position: absolute;
    left: 48px;
    top: 1090px;
    display: flex;
    align-items: center;
    gap: 18px;
  }
  .brand__mark {
    width: 58px;
    height: 58px;
    background: var(--ink-dark);
  }
  .brand__name {
    color: var(--ink-dark);
    font-weight: 800;
    font-size: 40px;
    line-height: 42px;
    letter-spacing: 0.5px;
  }
  .brand__tagline {
    color: var(--ink-dark);
    font-weight: 600;
    font-size: 21px;
    line-height: 26px;
  }
</style>
</head>
<body>
<main class="ad">
  <svg class="ad__chevrons" width="1200" height="100" viewBox="0 0 1200 100" aria-hidden="true">
    <polygon points="367,0 833,0 600,84" fill="var(--brand-red-light)"/>
    <polygon points="470,0 730,0 600,47" fill="#c42a2a"/>
  </svg>

  <h1 class="ad__headline">PROTECT AND CONCEAL HIGH<br>AND LOW VOLTAGE CONNECTIVITY</h1>

  <svg class="ad__dots ad__dots--left" width="180" height="100" viewBox="0 0 180 100" aria-hidden="true">
    <g fill="var(--dot)">
      <circle cx="8" cy="10" r="3.5"/><circle cx="49" cy="10" r="3.5"/><circle cx="90" cy="10" r="3.5"/><circle cx="131" cy="10" r="3.5"/><circle cx="172" cy="10" r="3.5"/>
      <circle cx="8" cy="51" r="3.5"/><circle cx="49" cy="51" r="3.5"/><circle cx="90" cy="51" r="3.5"/><circle cx="131" cy="51" r="3.5"/><circle cx="172" cy="51" r="3.5"/>
      <circle cx="8" cy="92" r="3.5"/><circle cx="49" cy="92" r="3.5"/><circle cx="90" cy="92" r="3.5"/><circle cx="131" cy="92" r="3.5"/><circle cx="172" cy="92" r="3.5"/>
    </g>
  </svg>
  <svg class="ad__dots ad__dots--right" width="180" height="100" viewBox="0 0 180 100" aria-hidden="true">
    <g fill="var(--dot)">
      <circle cx="8" cy="10" r="3.5"/><circle cx="49" cy="10" r="3.5"/><circle cx="90" cy="10" r="3.5"/><circle cx="131" cy="10" r="3.5"/><circle cx="172" cy="10" r="3.5"/>
      <circle cx="8" cy="51" r="3.5"/><circle cx="49" cy="51" r="3.5"/><circle cx="90" cy="51" r="3.5"/><circle cx="131" cy="51" r="3.5"/><circle cx="172" cy="51" r="3.5"/>
      <circle cx="8" cy="92" r="3.5"/><circle cx="49" cy="92" r="3.5"/><circle cx="90" cy="92" r="3.5"/><circle cx="131" cy="92" r="3.5"/><circle cx="172" cy="92" r="3.5"/>
    </g>
  </svg>

  <div class="ad__product-photo" role="img" aria-label="Photo of a black stage pocket floor box set into a wooden floor, with cables running out beside a lit evergreen garland"></div>

  <p class="ad__cta-label">Become a Dealer</p>
  <a class="ad__cta-button" href="#">CLICK HERE</a>

  <svg class="ad__footer" width="1200" height="1200" viewBox="0 0 1200 1200" aria-hidden="true">
    <polygon points="640,1130 1200,1130 1200,1200 640,1200" fill="var(--band-grey)"/>
    <polygon points="0,1067 604,1067 722,1200 0,1200" fill="var(--panel-grey)"/>
  </svg>

  <div class="brand">
    <div class="brand__mark"></div>
    <div class="brand__text">
      <div class="brand__name">TOVERMUNDIC CO</div>
      <div class="brand__tagline">Stage Pocket Systems Connectivity</div>
    </div>
  </div>
</main>
</body>
</html>
```